Business Card Design for Quorvane

Need a business card designed for Quorvane employees.
- 2 sided business card
- Front:
Company Logo (file attached)
Background could be:white with perhaps a red/black stripe on the left
OR
Background could be: OR dark red-black gradient: be creative
Include the following on the front:
Martin Delacroy
Founder & CEO
martin.delacroy@quorvane-example.com
+1 555.013.4782
quorvane-example.com
- Back: White color background with company logo
Text under the logo: Ledger Streamline 4.0
** be creative about the font, mix of upper and lower case and colors for the text **
Target Market(s)
We are a software company marketing our products to large and medium sized businesses.
Industry/Entity Type
Business

```html
<!DOCTYPE html>
<html lang="en">
<head>
<meta charset="utf-8">
<title>Quorvane – Business Card</title>
<link rel="stylesheet" href="https://fonts.googleapis.com/css2?family=Josefin+Sans:wght@400;600&display=swap">
<style>
  :root {
    --backdrop: #ebe6d3;
    --card: #fdfdfd;
    --ink: #1e1414;
    --red: #9c0a0e;
    --red-deep: #5e0205;
    --black: #0d0d0d;
    --shadow: rgba(60, 50, 30, 0.22);
  }
  * { box-sizing: border-box; margin: 0; padding: 0; }
  html, body {
    width: 1200px; height: 560px; overflow: hidden;
    background: var(--backdrop);
    font-family: "Josefin Sans", sans-serif;
    color: var(--ink);
  }
  .canvas {
    position: relative; width: 1200px; height: 560px;
    display: flex; align-items: center; justify-content: center; gap: 60px;
  }
  .card {
    position: relative; width: 510px; height: 292px;
    background: var(--card);
    box-shadow: 0 10px 28px var(--shadow);
    overflow: hidden;
  }

  /* Front */
  .card-front .stripe {
    position: absolute; left: 0; top: 0; bottom: 0; width: 64px;
    background: linear-gradient(180deg, var(--red) 0%, var(--red-deep) 100%);
  }
  .card-front .stripe-edge {
    position: absolute; left: 64px; top: 0; bottom: 0; width: 7px;
    background: var(--black);
  }
  .card-front .brand {
    position: absolute; left: 104px; top: 36px;
    display: flex; align-items: center; gap: 16px;
  }
  .brand-dot {
    width: 58px; height: 58px; border-radius: 50%;
    background: var(--ink);
  }
  .brand-name {
    font-weight: 400; font-size: 42px; letter-spacing: 3px;
    text-transform: uppercase; color: var(--ink); line-height: 1;
  }
  .tagline {
    color: var(--red); font-size: 14px; letter-spacing: 0.5px;
  }
  .card-front .tagline {
    position: absolute; left: 180px; top: 88px;
  }
  .person {
    position: absolute; left: 104px; top: 150px;
  }
  .person-name {
    font-size: 24px; font-weight: 400; text-transform: uppercase;
    letter-spacing: 0.5px; color: var(--ink); line-height: 1;
  }
  .person-role {
    font-size: 12px; color: var(--red); margin-top: 4px;
  }
  .contact {
    position: absolute; left: 116px; top: 206px;
    list-style: none; font-size: 15px; line-height: 1.2; color: var(--red-deep);
  }

  /* Back */
  .card-back .brand {
    position: absolute; left: 0; right: 0; top: 102px;
    display: flex; flex-direction: column; align-items: center;
  }
  .card-back .brand-name {
    font-size: 62px; letter-spacing: 5px;
  }
  .card-back .tagline {
    margin-top: 12px; font-size: 13px; letter-spacing: 4px;
    text-transform: uppercase;
  }
</style>
</head>
<body>
<main class="canvas">
  <section class="card card-back" aria-label="Card back">
    <div class="brand">
      <span class="brand-name">Quorvane</span>
      <span class="tagline">Ledger Streamline 4.0</span>
    </div>
  </section>

  <section class="card card-front" aria-label="Card front">
    <div class="stripe"></div>
    <div class="stripe-edge"></div>
    <div class="brand">
      <span class="brand-dot"></span>
      <span class="brand-name">Quorvane</span>
    </div>
    <span class="tagline">Ledger Streamline 4.0</span>
    <div class="person">
      <h1 class="person-name">Martin Delacroy</h1>
      <p class="person-role">Founder &amp; CEO</p>
    </div>
    <ul class="contact">
      <li>martin.delacroy@quorvane-example.com</li>
      <li>+1 555.013.4782</li>
      <li>quorvane-example.com</li>
    </ul>
  </section>
</main>
</body>
</html>
```